Music Festival Business Cards

The Lanternmoor Festival
Produced by Bramblewick Sound Group LLC
New music festival in Arkansas.

Target Market(s)

18-35 year olds

Industry/Entity Type

Festival

Contact Information for Business Card

We are a 5-partner team producing a music festival in Arkansas. We need slick business cards, and I want them to be square.

Requirements
Must have
• I NEED THESE TO BE IN SQUARE SIZE - 2x2 or 2.5x2.5... please not regular size.
• I need www.thelanternmoor.live as the link to website.

```html
<!DOCTYPE html>
<html lang="en">
<head>
<meta charset="utf-8">
<title>The Lanternmoor Festival – Square Business Card</title>
<link rel="stylesheet" href="https://fonts.googleapis.com/css2?family=Open+Sans:wght@400;600;700&display=swap">
<style>
  :root {
    --page: #e9e6e1;
    --card: #050607;
    --card-band: #0c1415;
    --teal: #45c4cc;
    --white: #f2f4f4;
    --rule: #3a3d40;
    --silver: #c9cdd0;
  }
  * { margin: 0; padding: 0; box-sizing: border-box; }
  html, body {
    width: 1200px; height: 1200px; overflow: hidden;
    background: var(--page);
    font-family: "Open Sans", Arial, sans-serif;
  }
  .sheet {
    position: relative; width: 1200px; height: 1200px;
    display: flex; flex-direction: row; align-items: center; justify-content: center; gap: 40px;
  }
  .card {
    position: relative; width: 540px; height: 540px; flex: none;
    background: var(--card); overflow: hidden;
    box-shadow: 0 10px 30px rgba(0,0,0,0.18);
  }
  .card-front .top-band {
    position: absolute; left: 0; top: 0; width: 100%; height: 36px;
    background: var(--card-band);
  }
  .card-front .accent-block {
    position: absolute; left: 0; top: 36px; width: 44px; height: 40px;
    background: var(--teal);
  }
  .card-front .divider {
    position: absolute; inset: 0; width: 100%; height: 100%;
  }
  .holder { position: absolute; left: 60px; top: 32px; }
  .holder-name {
    color: var(--teal); font-weight: 600; font-size: 40px; letter-spacing: 0.5px; line-height: 1.15;
  }
  .holder-role { color: var(--white); font-size: 20px; margin-top: 2px; }
  .brand-name {
    position: absolute; right: 36px; top: 300px;
    color: var(--teal); font-weight: 700; font-size: 34px; letter-spacing: 2px; white-space: nowrap;
  }
  .contact-list {
    position: absolute; right: 36px; bottom: 36px; list-style: none; text-align: right;
  }
  .contact-list li {
    display: flex; align-items: center; justify-content: flex-end; gap: 10px;
    color: var(--white); font-size: 17px; line-height: 28px; white-space: nowrap;
  }
  .contact-list svg { width: 16px; height: 16px; flex: none; }
  .card-back {
    background: linear-gradient(135deg, #000 0%, #050505 45%, #2a2a2a 100%);
    display: flex; align-items: center; justify-content: center;
  }
  .back-brand {
    color: var(--silver); font-weight: 700; font-size: 36px; letter-spacing: 4px; white-space: nowrap;
  }
</style>
</head>
<body>
<main class="sheet">
  <section class="card card-front">
    <div class="top-band"></div>
    <div class="accent-block"></div>
    <svg class="divider" viewBox="0 0 540 540" aria-hidden="true">
      <line x1="0" y1="330" x2="540" y2="90" stroke="var(--rule)" stroke-width="1.5"/>
    </svg>
    <div class="holder">
      <p class="holder-name">MARA ELLISON</p>
      <p class="holder-role">Director</p>
    </div>
    <p class="brand-name">THE LANTERNMOOR</p>
    <ul class="contact-list">
      <li>1-479-555-0182
        <svg viewBox="0 0 24 24"><path fill="var(--teal)" d="M6.6 10.8a15 15 0 0 0 6.6 6.6l2.2-2.2a1 1 0 0 1 1-.25 11.4 11.4 0 0 0 3.6.57 1 1 0 0 1 1 1V20a1 1 0 0 1-1 1A17 17 0 0 1 3 4a1 1 0 0 1 1-1h3.5a1 1 0 0 1 1 1c0 1.25.2 2.45.57 3.57a1 1 0 0 1-.25 1z"/></svg></li>
      <li>www.thelanternmoor.live
        <svg viewBox="0 0 24 24"><circle cx="12" cy="12" r="9" fill="none" stroke="var(--teal)" stroke-width="2"/><path d="M3 12h18M12 3c3 3 3 15 0 18M12 3c-3 3-3 15 0 18" fill="none" stroke="var(--teal)" stroke-width="1.6"/></svg></li>
      <li>mara@thelanternmoor.live
        <svg viewBox="0 0 24 24"><rect x="2" y="5" width="20" height="14" rx="1" fill="var(--teal)"/><path d="M2 6l10 7 10-7" fill="none" stroke="var(--card)" stroke-width="1.6"/></svg></li>
      <li>Fayetteville, Arkansas
        <svg viewBox="0 0 24 24"><path fill="var(--teal)" d="M12 2a7 7 0 0 0-7 7c0 5 7 13 7 13s7-8 7-13a7 7 0 0 0-7-7zm0 9.5A2.5 2.5 0 1 1 12 6.5a2.5 2.5 0 0 1 0 5z"/></svg></li>
    </ul>
  </section>

  <section class="card card-back">
    <p class="back-brand">THE LANTERNMOOR</p>
  </section>
</main>
</body>
</html>
```